Redesign current website

Current website www.kelvatreproperty.com.au needs to be redone.

Content will be the same however the visual look needs to be upgraded.

Need ability to WYSIWYG editor any of the pages, including embedding videos and images throughout the pages.

It currently looks dated and a bit dodgy. Need the same functionality (i.e. submission forms etc...) however need it to look much more modern.

Needs to be easy to navigate, and look fresh, credible and professional.

Must be mobile compatible and SEO friendly.

Not interested in sites that look like the 1000+ one websites templates.

```html
<!DOCTYPE html>
<html lang="en">
<head>
<meta charset="utf-8">
<title>Kelvatre Home Buyers</title>
<link href="https://fonts.googleapis.com/css2?family=Raleway:wght@400;500;600&family=Open+Sans:wght@400;600&display=swap" rel="stylesheet">
<style>
:root{
  --blue:#1f3fa6;
  --blue-dark:#17318a;
  --navy:#1d2f8c;
  --orange:#f2a20c;
  --orange-light:#f7b820;
  --cyan:#10d3ee;
  --text:#555;
  --dark:#333;
  --line:#dcdcdc;
  --footer:#f1f1f1;
}
*{box-sizing:border-box;margin:0;padding:0}
html,body{width:806px;height:1200px;overflow:hidden;background:#fff}
body{position:relative;font-family:"Open Sans",Arial,sans-serif;color:var(--text)}
.abs{position:absolute}
.heading{font-family:"Raleway",Arial,sans-serif}

/* header */
.brand{left:121px;top:24px;display:flex;align-items:center;gap:8px}
.brand-dot{width:30px;height:30px;border-radius:50%;background:var(--blue)}
.brand-name{font-family:"Raleway",sans-serif;font-weight:600;font-size:22px;color:var(--blue)}
.enquiry{right:124px;top:28px;text-align:right}
.enquiry small{display:block;font-size:10px;color:var(--navy)}
.enquiry .phone{font-family:"Raleway",sans-serif;font-size:17px;color:var(--navy);display:flex;align-items:center;gap:4px;justify-content:flex-end}

/* nav */
.nav{left:0;top:71px;width:806px;height:35px;background:linear-gradient(#2b54c4,var(--blue-dark))}
.nav ul{list-style:none;display:flex;position:absolute;left:112px;top:0;height:35px}
.nav li{font-family:"Raleway",sans-serif;font-size:10.5px;font-weight:500;color:#fff;height:35px;line-height:35px;text-align:center;border-right:1px solid rgba(255,255,255,.18)}
.nav li:last-child{border-right:none}

/* hero */
.hero{left:0;top:106px;width:806px;height:273px;background:linear-gradient(90deg,#e7e4e2 0%,#f2f1f0 45%,#e4e5ea 100%)}
.hero-kicker{left:117px;top:181px;font-size:16px;color:var(--orange)}
.hero-title{left:117px;top:199px;font-size:23px;color:var(--navy);font-weight:500}
.hero-text{left:119px;top:234px;font-size:7px;line-height:12px;color:#555}
.btn{background:linear-gradient(var(--orange-light),var(--orange));color:#fff;text-align:center;font-size:8.5px}
.hero-btn{left:118px;top:268px;width:106px;height:24px;line-height:24px;font-size:9.5px}
.video{left:422px;top:153px;width:264px;height:164px;background:#fff;box-shadow:0 0 3px rgba(0,0,0,.25);padding:6px}
.video-area{width:100%;height:100%;background:linear-gradient(#1a1a1a,#000);position:relative}
.play{position:absolute;left:116px;top:59px}
.arrow{top:210px}

/* features */
.feature{top:410px;width:180px;text-align:center}
.feature h3{font-family:"Raleway",sans-serif;font-weight:500;font-size:14px;color:var(--navy);margin:8px 0 6px}
.feature p{font-size:6.3px;line-height:10.7px;color:#555}
.feature .btn{width:64px;height:18px;line-height:18px;margin:12px auto 0}
.divider{left:0;top:577px;width:806px;height:1px;background:var(--line)}

/* about */
.about-title{left:120px;top:617px;font-size:21px;color:var(--dark)}
.about-text{left:120px;top:654px;width:375px;font-size:6.8px;line-height:9.8px;color:#555}
.about-text p{margin-bottom:5px}
.lender{left:522px;top:615px;width:170px;height:186px;border:1px solid var(--line)}
.lender-head{height:31px;background:var(--navy);color:#fff;font-family:"Raleway",sans-serif;font-size:13px;line-height:31px;padding-left:16px}
.field{position:absolute;left:14px;width:143px;height:18px;border:1px solid var(--line);background:linear-gradient(#fafafa,#eee);font-size:6px;color:#777;padding:4px 7px}
.submit{position:absolute;left:14px;top:155px;width:60px;height:19px;line-height:19px;font-size:10px}

/* panels */
.panel{top:829px;height:147px;border:1px solid var(--line)}
.panel-head{height:27px;color:#fff;font-family:"Raleway",sans-serif;font-size:12.5px;line-height:27px;padding-left:16px}
.feed{left:119px;width:279px}
.feed .panel-head{background:var(--cyan)}
.tweet{position:absolute;left:15px;display:flex;gap:8px}
.avatar{width:23px;height:23px;background:linear-gradient(#d8b9a0,#8a6a55);flex:none}
.tweet p{font-size:6.3px;line-height:9.8px;color:#555;width:215px}
.tweet .time{color:var(--blue);display:block}
.solutions{left:409px;width:278px}
.solutions .panel-head{background:var(--orange)}
.sol-list{position:absolute;top:44px;list-style:none;font-size:7.2px;color:#666}
.sol-list li{height:17.6px}
.sol-list li::before{content:"›";margin-right:6px;color:#777}

/* footer */
.footer{left:0;top:1016px;width:806px;height:149px;background:linear-gradient(#e9e9e9,var(--footer) 20%)}
.fcol{top:1046px}
.fcol h4{font-family:"Open Sans",sans-serif;font-weight:400;font-size:9.5px;color:#222;margin-bottom:3px}
.fcol li{list-style:none;font-size:7.5px;line-height:13.6px;color:#444}
.fsep{top:1046px;width:1px;height:84px;background:#ddd}
.social{display:flex;gap:3px;margin-top:3px}
.social span{width:10px;height:10px;background:var(--navy);border-radius:1px}
.bottom{left:0;top:1166px;width:806px;height:34px;background:#fff}
.copy{left:121px;top:1180px;font-size:6.5px;color:#444}
</style>
</head>
<body>

<div class="abs brand"><span class="brand-dot"></span><span class="brand-name">Kelvatre Home Buyers</span></div>
<div class="abs enquiry">
  <small>For Enquiry Now</small>
  <div class="phone">
    <svg width="13" height="13" viewBox="0 0 24 24"><path fill="#f2a20c" d="M6.6 10.8a15 15 0 0 0 6.6 6.6l2.2-2.2c.3-.3.7-.4 1-.2 1.1.4 2.3.6 3.6.6.6 0 1 .4 1 1V20c0 .6-.4 1-1 1A17 17 0 0 1 3 4c0-.6.4-1 1-1h3.5c.6 0 1 .4 1 1 0 1.3.2 2.5.6 3.6.1.3 0 .7-.2 1z"/></svg>
    1800 555 019
  </div>
</div>

<nav class="abs nav"><ul>
  <li style="width:70px">HOME</li>
  <li style="width:88px">ABOUT US</li>
  <li style="width:120px">OUR SOLUTIONS</li>
  <li style="width:114px">HOW IT WORKS</li>
  <li style="width:86px">SUPPORT</li>
  <li style="width:103px">CONTACT US</li>
</ul></nav>

<section class="abs hero" role="img" aria-label="Photo of a row of terraced houses under a pale sky"></section>
<div class="abs hero-kicker heading">Suspendisse quam leo molestie</div>
<h1 class="abs hero-title heading">Fusce ultricies orci feugiat</h1>
<p class="abs hero-text">Etiam nulla massa pharetra facilisis volutpat in imperdiet sit amet sem<br>Aliquam nec erat at purus cursus interdum</p>
<div class="abs btn hero-btn">Sell Your Property</div>
<div class="abs video">
  <div class="video-area" role="img" aria-label="Introductory video from the company director">
    <svg class="play" width="30" height="30" viewBox="0 0 30 30"><circle cx="15" cy="15" r="15" fill="#fff"/><path d="M12 9l9 6-9 6z" fill="#000"/></svg>
  </div>
</div>
<svg class="abs arrow" style="left:62px" width="16" height="42" viewBox="0 0 16 42"><path d="M15 1L1 21l14 20" fill="none" stroke="#333" stroke-width="1.2"/></svg>
<svg class="abs arrow" style="left:715px" width="16" height="42" viewBox="0 0 16 42"><path d="M1 1l14 20L1 41" fill="none" stroke="#333" stroke-width="1.2"/></svg>

<div class="abs feature" style="left:115px;top:413px">
  <svg width="36" height="26" viewBox="0 0 36 26"><rect x="1.5" y="1.5" width="33" height="23" rx="2" fill="none" stroke="#1d2f8c" stroke-width="3"/><circle cx="18" cy="13" r="6" fill="#1d2f8c"/><text x="18" y="16.5" font-size="9" fill="#fff" text-anchor="middle" font-family="Arial">1</text></svg>
  <h3>Fast Money</h3>
  <p>We've bought property in as little as seven (7) days. If you call us early enough, we can save you from bankruptcy, foreclosure or repossession. 7 day cash doesn't give you the best price, but it does give you CERTAINTY!</p>
  <div class="btn">Read More</div>
</div>
<div class="abs feature" style="left:309px">
  <svg width="38" height="32" viewBox="0 0 38 32"><path d="M2 2v28h34" fill="none" stroke="#1d2f8c" stroke-width="2.5"/><path d="M6 25l9-9 6 5 12-13" fill="none" stroke="#1d2f8c" stroke-width="3"/><path d="M27 6h8v8z" fill="#1d2f8c"/></svg>
  <h3>Maximum Profit</h3>
  <p>We've bought property in as little as seven (7) days. If you call us early enough, we can save you from bankruptcy, foreclosure or repossession. 7 day cash doesn't give you the best price, but it does give you CERTAINTY!</p>
  <div class="btn">Read More</div>
</div>
<div class="abs feature" style="left:505px">
  <svg width="32" height="32" viewBox="0 0 32 32"><circle cx="16" cy="16" r="16" fill="#1d2f8c"/><path d="M8 16l6 6 11-11" fill="none" stroke="#fff" stroke-width="4"/></svg>
  <h3>Benefits</h3>
  <p>We've bought property in as little as seven (7) days. If you call us early enough, we can save you from bankruptcy, foreclosure or repossession. 7 day cash doesn't give you the best price, but it does give you CERTAINTY!</p>
  <div class="btn">Read More</div>
</div>
<div class="abs divider"></div>

<h2 class="abs about-title heading" style="font-weight:400">About Our Company</h2>
<div class="abs about-text">
  <p>Kelvatre Home Buyers (AUST) Pty Ltd are not real estate agents wanting to list your real estate for sale. Kelvatre Home Buyers (AUST) Pty Ltd are professional property investors who buy property for a living.</p>
  <p>We actually purchase the property.</p>
  <p>We purchase the property in either our own name, in the name of one of our Trusts, or in the name of one of our affiliated clients who are also looking to purchase. We are motivated buyers who want to deal with motivated sellers.</p>
  <p>No need to deal with a "middle man" real estate agent who will charge you fees; to advertise your property (and their real estate agency) and then charge you even more fees if they manage to sell your property after many months on the market.</p>
  <p>With Kelvatre Home Buyers (AUST) Pty Ltd, there are no fees and no fuss. Why no fees? Because we are not performing a service for you...we are simply buying your property from you.</p>
</div>

<form class="abs lender">
  <div class="lender-head">Private Lender Alert</div>
  <div class="field" style="top:46px">Name</div>
  <div class="field" style="top:69px">Email</div>
  <div class="field" style="top:93px">Phone</div>
  <div class="field" style="top:116px;height:34px">Message</div>
  <div class="btn submit">Submit</div>
</form>

<div class="abs panel feed">
  <div class="panel-head">Social Feed</div>
  <div class="tweet" style="top:40px">
    <div class="avatar" role="img" aria-label="Profile photo"></div>
    <p><span style="color:#333">Lorem ipsum dolor sit amet consectetuer</span> @ iln massa libero interdum nec interdum vel blandit sed nulla In ullamcorper est eget tempor cursus neque mi consectetuer mi a ultricies massa est sed nisl Class aptent taciti sociosqu ad litora torquent<span class="time">2 days ago</span></p>
  </div>
  <div class="tweet" style="top:100px">
    <div class="avatar" role="img" aria-label="Profile photo"></div>
    <p><span style="color:#333">Quisque dignissim congue</span> @ inIn massa libero interdum nec interdum vel blandit sed nulla In ullamcorper est eget tempor cursus neque mi consectetuer mi a ultrici<span class="time">2 days ago</span></p>
  </div>
</div>

<div class="abs panel solutions">
  <div class="panel-head">Our Solutions</div>
  <ul class="sol-list" style="left:18px">
    <li>Fast Cash</li><li>Normal Sale</li><li>Short Settlement</li><li>Long Settlement</li><li>Profit Sharing</li>
  </ul>
  <ul class="sol-list" style="left:130px">
    <li>Sell and Rent Back</li><li>Sell the Debt / Keep the Income</li><li>Joint Venture</li><li>Develop Together</li><li>ANY Reasonable Agreement</li>
  </ul>
</div>

<footer class="abs footer"></footer>
<div class="abs fcol" style="left:126px"><h4>COMPANY</h4><ul><li>Home</li><li>About Us</li><li>Our Solutions</li><li>Services</li><li>FAQ</li></ul></div>
<div class="abs fsep" style="left:204px"></div>
<div class="abs fcol" style="left:234px"><h4>SERVICES</h4><ul><li>Suspendisse quam</li><li>Leo molestie sed</li><li>Auctus quis feugiat</li><li>Fusce tellus</li><li>Sed metus augue</li></ul></div>
<div class="abs fsep" style="left:331px"></div>
<div class="abs fcol" style="left:375px"><h4>RESOURCES</h4><ul><li>Recent Blogs</li><li>Support</li><li>Term of Use</li><li>Contact Us</li></ul></div>
<div class="abs fsep" style="left:482px"></div>
<div class="abs fcol" style="left:522px"><h4>CONTACT US</h4><ul><li>42 Harbour Lane, Suite 3, Brisbane QLD 4000</li><li>07 5550 1287</li><li>info@kelvatreproperty.com.au</li></ul>
  <div class="social"><span></span><span></span><span></span></div>
</div>

<div class="abs bottom"></div>
<div class="abs copy">© 2015 Company Name &nbsp;All right reserved &nbsp;Term of Use</div>

</body>
</html>
```